Trade show booth design in Vector format.

Hello, I need a tradeshow booth design for a company called Valorine. I am in need of a background for a dental trade show I will be doing in 10 days. The format is 90" by 90" with a .25 bleed.

Here are my 2 websites with the products and services I offer, I think this can give you a good idea of the colors and styles of font we like.

www.clearvats.ca

http://valorine.example-sites.com

I'm thinking the type of theme of the background being the water theme I posted 1.1 MB file - with the phrase

"Des Solutions de traitement de l'eau efficaces et fiables pour votre clinique dentaire"

As the title text.

- with my 2 comapny logos integrated.

I am in need of this ASAP, so lets get going.

Raffaele

Target Market(s)

Dentists

Industry/Entity Type

Water Purification

Font styles to use
Sans Serif

Colors
33a6d7
85cae6
cee9f5
0692cd

Requirements
Must have
• My 2 logos - for my 2 companies.
• The slogan
• Des Solutions de traitement de l'eau efficaces et fiables pour votre clinique dentaire

```html
<!DOCTYPE html>
<html lang="fr">
<head>
<meta charset="utf-8">
<title>Valorine – Trade Show Backdrop</title>
<link href="https://fonts.googleapis.com/css2?family=Montserrat:wght@300;400;900&display=swap" rel="stylesheet">
<style>
  :root {
    --blue-deep: #0692cd;
    --blue-mid: #33a6d7;
    --blue-soft: #85cae6;
    --blue-pale: #cee9f5;
    --white: #ffffff;
    --teal: #2fa6a4;
  }
  html, body {
    margin: 0;
    padding: 0;
    width: 1200px;
    height: 1200px;
    overflow: hidden;
    background: var(--white);
  }
  .backdrop {
    position: relative;
    width: 1200px;
    height: 1200px;
    overflow: hidden;
    font-family: "Montserrat", sans-serif;
  }
  .water-photo {
    position: absolute;
    inset: 0;
    background:
      linear-gradient(180deg,
        #eef2f5 0%,
        #e3e8ec 7%,
        var(--blue-mid) 12%,
        var(--blue-deep) 16%,
        var(--blue-soft) 21%,
        var(--blue-pale) 30%,
        #e4f1f8 50%,
        var(--blue-pale) 75%,
        #d6ecf6 100%);
  }
  .headline {
    position: absolute;
    top: 340px;
    left: 0;
    width: 1200px;
    margin: 0;
    text-align: center;
    font-weight: 900;
    color: var(--blue-deep);
    letter-spacing: 1px;
    text-shadow:
      -3px -3px 0 var(--white), 3px -3px 0 var(--white),
      -3px 3px 0 var(--white), 3px 3px 0 var(--white),
      0 6px 10px rgba(0, 60, 100, 0.35);
  }
  .headline .line { display: block; line-height: 1.02; }
  .headline .big { font-size: 82px; }
  .headline .small { font-size: 50px; font-weight: 400; }
  .logo-band {
    position: absolute;
    top: 690px;
    left: 120px;
    width: 960px;
    height: 130px;
    background: rgba(255, 255, 255, 0.72);
    display: flex;
    align-items: center;
    justify-content: center;
    gap: 150px;
  }
  .brand {
    display: flex;
    align-items: center;
    gap: 16px;
    font-weight: 300;
    color: var(--teal);
  }
  .brand-mark-circle {
    width: 34px;
    height: 34px;
    border-radius: 50%;
    background: var(--teal);
  }
  .brand-mark-square {
    width: 30px;
    height: 30px;
    background: var(--teal);
  }
  .brand-valorine { font-size: 52px; letter-spacing: 2px; }
  .brand-clearvats { font-size: 34px; letter-spacing: 2px; }
</style>
</head>
<body>
<main class="backdrop">
  <div class="water-photo" role="img" aria-label="Photo of clear blue water with a rippling surface near the top and rising air bubbles"></div>

  <h1 class="headline">
    <span class="line big"><span class="small">Des</span> Solutions</span>
    <span class="line big">de traitement de l'eau</span>
    <span class="line"><span class="small">efficaces et</span> <span class="big">fiables</span> <span class="small">pour votre</span></span>
    <span class="line big">clinique dentaire</span>
  </h1>

  <section class="logo-band">
    <div class="brand">
      <span class="brand-mark-circle"></span>
      <span class="brand-valorine">valorine</span>
    </div>
    <div class="brand">
      <span class="brand-mark-square"></span>
      <span class="brand-clearvats">CLEAR VATS</span>
    </div>
  </section>
</main>
</body>
</html>
```